Customer flyer

Hi there,

We need a flyer done for our father's business. It is called Tidal crest and the flyer will be distributed to realtors in British Columbia. He lends money to realtors when they have sold a home from the time subjects are removed from the transaction to when the sale closes. He is looking for a modern, classy look with the following information:

"Tidal Crest"

Realtor Pay Day upon Subject Removal

Did you know?

* Fees 100% tax deductable
* Same Day Service
* Confidential
* Low Rates

Your money from 738519 B.C. Ltd. and It can be directly deposited into your bank account or delivered to your office

For quote: call Gavin Merrow 250 555 0137

This is a small business so he doesn't have a logo and has never needed to do promotions before as it's run on word of mouth for the past 10 years. We are open to all ideas and suggestions - he is a finance guy so looking to you for the creative side :)

Thank you!

I don't like the phrase Realtor Pay Day upon subject removal. I think I prefer "Realtors! Celebrate Your Home sales upon subject removal" . Your thoughts?

Thank you

```html
<!DOCTYPE html>
<html lang="en">
<head>
<meta charset="utf-8">
<title>Tidal Crest – Realtor Flyer</title>
<link rel="stylesheet" href="https://fonts.googleapis.com/css2?family=Oswald:wght@700&family=Carlito:wght@700&display=swap">
<style>
  :root {
    --page-bg: #e4e0da;
    --brand-blue: #2f5f9b;
    --band-grey: #c6c8cb;
    --paper: #ffffff;
    --ink: #111111;
    --photo-warm: #e8d2bf;
    --photo-pale: #f6ede5;
  }
  * { margin: 0; padding: 0; box-sizing: border-box; }
  html, body { width: 870px; height: 1200px; overflow: hidden; }
  body {
    background: var(--page-bg);
    font-family: "Carlito", "Calibri", sans-serif;
    font-weight: 700;
    color: var(--ink);
    position: relative;
  }
  .flyer {
    position: absolute;
    left: 169px; top: 33px;
    width: 532px; height: 1134px;
    background: var(--paper);
    overflow: hidden;
  }
  .masthead {
    position: absolute; left: 0; top: 0;
    width: 100%; height: 266px;
    background: var(--brand-blue);
    color: var(--paper);
    text-align: center;
    font-family: "Oswald", sans-serif;
    font-weight: 700;
  }
  .masthead .name-main {
    position: absolute; left: 0; right: 0; top: 14px;
    font-size: 138px; line-height: 1;
    letter-spacing: 2px;
  }
  .masthead .rule {
    position: absolute; left: 63px; right: 76px; top: 175px;
    height: 9px; background: var(--paper);
  }
  .masthead .name-sub {
    position: absolute; left: 63px; right: 76px; top: 188px;
    font-size: 48px; line-height: 1;
    letter-spacing: 0.42em; padding-left: 0.42em;
    font-weight: 400;
  }
  .band-grey {
    position: absolute; left: 0; width: 100%;
    background: var(--band-grey);
  }
  .band-grey.top { top: 266px; height: 19px; }
  .band-grey.bottom { top: 1102px; height: 17px; }
  .tagline {
    position: absolute; left: 0; right: 0; top: 315px;
    text-align: center; font-size: 27px; line-height: 34px;
  }
  .headline {
    position: absolute; left: 0; right: 0; top: 370px;
    text-align: center; font-size: 68px; line-height: 76px;
  }
  .photo-area {
    position: absolute; left: 0; top: 488px;
    width: 200px; height: 285px;
    background: linear-gradient(135deg, var(--photo-warm), var(--photo-pale));
  }
  .benefit {
    position: absolute; left: 268px;
    font-size: 28px; line-height: 34px;
  }
  .tick {
    position: absolute; left: 208px;
    width: 52px; height: 42px;
  }
  .note {
    position: absolute; left: 20px; right: 20px; top: 815px;
    text-align: center; font-size: 21px; line-height: 30px;
  }
  .contact {
    position: absolute; left: 0; top: 939px;
    width: 100%; height: 157px;
    background: var(--brand-blue);
    color: var(--paper);
    text-align: center;
  }
  .contact .call { position: absolute; left: 0; right: 0; top: 36px; font-size: 26px; line-height: 34px; }
  .contact .phone { position: absolute; left: 0; right: 0; top: 70px; font-size: 34px; line-height: 40px; letter-spacing: 1px; }
</style>
</head>
<body>
  <main class="flyer">
    <header class="masthead">
      <div class="name-main">TIDAL</div>
      <div class="rule"></div>
      <div class="name-sub">CREST</div>
    </header>
    <div class="band-grey top"></div>

    <p class="tagline">Realtor Pay Day upon Subject Removal</p>
    <h1 class="headline">did YOU know?</h1>

    <div class="photo-area" role="img" aria-label="Photo of a hand giving a thumbs up"></div>

    <svg class="tick" style="top:498px" viewBox="0 0 52 42"><path d="M1 24 L10 17 L20 28 L46 1 L51 6 L20 41 Z" fill="#111"/></svg>
    <p class="benefit" style="top:477px">Fees 100%<br>tax deductable</p>

    <svg class="tick" style="top:594px" viewBox="0 0 52 42"><path d="M1 24 L10 17 L20 28 L46 1 L51 6 L20 41 Z" fill="#111"/></svg>
    <p class="benefit" style="top:580px">Same Day Service</p>

    <svg class="tick" style="top:662px" viewBox="0 0 52 42"><path d="M1 24 L10 17 L20 28 L46 1 L51 6 L20 41 Z" fill="#111"/></svg>
    <p class="benefit" style="top:648px">Confidential</p>

    <svg class="tick" style="top:730px" viewBox="0 0 52 42"><path d="M1 24 L10 17 L20 28 L46 1 L51 6 L20 41 Z" fill="#111"/></svg>
    <p class="benefit" style="top:716px">Low Rates</p>

    <p class="note">Your money from 738519 B.C. Ltd. and It<br>can be directly deposited into your bank<br>account or delivered to your office.</p>

    <footer class="contact">
      <p class="call">For quote: call Gavin Merrow</p>
      <p class="phone">250 555 0137</p>
    </footer>
    <div class="band-grey bottom"></div>
  </main>
</body>
</html>
```